I need a business card design for a new company that will be doing consulting work around issues of cultural competency, and diversity and inclusion. I would like the design to be crisp and clear with bold but conservative colors and incorporate shades of blue

Target Market(s)

Small businesses, schools, non-profits

Industry/Entity Type

Consulting

Font styles to use
Serif
Sans Serif

Colors
0c5ba6
6b449b
3276b5
0292cd

Requirements
Must have
• A Morrow Venture (name of company)
• Lemlem Tavish
• CEO
• lemlem@amorrowventure.com
• (215)483-2756

```html
<!DOCTYPE html>
<html lang="en">
<head>
<meta charset="utf-8">
<title>A Morrow Venture — Business Card</title>
<link rel="stylesheet" href="https://fonts.googleapis.com/css2?family=Cinzel:wght@600&family=Arimo:wght@400&display=swap">
<style>
  :root {
    --page-bg: #e9edf3;
    --brand-navy: #0c5ba6;
    --brand-purple: #6b449b;
    --brand-blue: #3276b5;
    --brand-sky: #0292cd;
    --card-light: #ffffff;
    --card-light-edge: #eef3f9;
    --ink: #1b2a3d;
    --paper-text: #ffffff;
  }
  * { box-sizing: border-box; margin: 0; padding: 0; }
  html, body {
    width: 1200px;
    height: 900px;
    overflow: hidden;
  }
  body {
    position: relative;
    background: var(--page-bg);
    color: var(--ink);
  }
  .card {
    position: absolute;
    width: 556px;
    height: 343px;
    box-shadow: 0 2px 8px rgba(12, 40, 80, 0.18);
    overflow: hidden;
  }
  .card--front {
    left: 330px;
    top: 90px;
    background: linear-gradient(160deg, var(--card-light) 0%, var(--card-light-edge) 100%);
    border-bottom: 8px solid var(--brand-navy);
  }
  .card--back {
    left: 330px;
    top: 470px;
    background: linear-gradient(135deg, var(--brand-sky) 0%, var(--brand-navy) 50%, var(--brand-purple) 100%);
    color: var(--paper-text);
  }

  .contact {
    position: absolute;
    inset: 0;
    text-align: center;
  }
  .contact__name {
    position: absolute;
    top: 98px;
    left: 0;
    width: 100%;
    font-family: "Cinzel", Georgia, serif;
    font-weight: 600;
    font-size: 25px;
    line-height: 30px;
    letter-spacing: 0.5px;
    color: var(--brand-navy);
  }
  .contact__title {
    position: absolute;
    top: 131px;
    left: 0;
    width: 100%;
    font-family: "Arimo", Arial, sans-serif;
    font-size: 18px;
    line-height: 22px;
    color: var(--brand-purple);
  }
  .contact__rule {
    position: absolute;
    top: 170px;
    left: 181px;
    width: 193px;
    height: 1px;
    background: var(--brand-blue);
  }
  .contact__line {
    position: absolute;
    left: 0;
    width: 100%;
    font-family: "Arimo", Arial, sans-serif;
    font-size: 18px;
    line-height: 22px;
    color: var(--ink);
  }
  .contact__phone { top: 197px; }
  .contact__email { top: 221px; }

  .brand {
    position: absolute;
    inset: 0;
  }
  .brand__mark {
    position: absolute;
    left: 228px;
    top: 76px;
  }
  .brand__name {
    position: absolute;
    top: 206px;
    left: 0;
    width: 100%;
    text-align: center;
    font-family: "Cinzel", Georgia, serif;
    font-weight: 600;
    font-size: 34px;
    line-height: 40px;
    letter-spacing: 1px;
    color: var(--paper-text);
  }
</style>
</head>
<body>
  <section class="card card--front" aria-label="Card front">
    <div class="contact">
      <p class="contact__name">LEMLEM TAVISH</p>
      <p class="contact__title">CEO</p>
      <div class="contact__rule"></div>
      <p class="contact__line contact__phone">(215)483-2756</p>
      <p class="contact__line contact__email">lemlem@amorrowventure.com</p>
    </div>
  </section>

  <section class="card card--back" aria-label="Card back">
    <div class="brand">
      <svg class="brand__mark" width="100" height="100" viewBox="0 0 100 100" aria-hidden="true">
        <circle cx="50" cy="50" r="42" fill="none" stroke="#ffffff" stroke-width="10"/>
      </svg>
      <p class="brand__name">A MORROW VENTURE</p>
    </div>
  </section>
</body>
</html>
```